Design a Banner for wood website

Need a 1345px by 400px banner (layered photoshop file w/png) created for a company that sells ipe wood decking.
- Must show ipe wood images within the design
- Must have text stating "Get a Quote!"

```html
<!DOCTYPE html>
<html lang="en">
<head>
<meta charset="utf-8">
<title>IPE Wood Decking Banner</title>
<link href="https://fonts.googleapis.com/css2?family=Source+Sans+3:wght@600;700&display=swap" rel="stylesheet">
<style>
  :root {
    --wood-dark: #5e3820;
    --wood-mid: #8a5430;
    --wood-warm: #a86a3c;
    --wood-light: #c08050;
    --headline: #ffffff;
    --button-top: #f6b865;
    --button-bottom: #c97a26;
    --button-edge: #a8621c;
    --arrow: #fbe3c2;
  }
  html, body {
    margin: 0;
    padding: 0;
    overflow: hidden;
    background: #ffffff;
  }
  .banner {
    position: relative;
    width: 1200px;
    height: 357px;
    overflow: hidden;
    font-family: "Source Sans 3", "Myriad Pro", Arial, sans-serif;
  }
  .banner__decking {
    position: absolute;
    inset: 0;
    background:
      linear-gradient(120deg, rgba(255,255,255,0.06) 0%, rgba(0,0,0,0.10) 50%, rgba(255,255,255,0.05) 100%),
      linear-gradient(45deg, var(--wood-dark) 0%, var(--wood-mid) 30%, var(--wood-warm) 55%, var(--wood-mid) 75%, var(--wood-light) 100%);
  }
  .banner__headline {
    position: absolute;
    left: 136px;
    top: 88px;
    margin: 0;
    font-size: 128px;
    font-weight: 600;
    line-height: 1;
    letter-spacing: -2px;
    color: var(--headline);
    text-shadow: 0 3px 8px rgba(40, 20, 8, 0.45);
    white-space: nowrap;
  }
  .banner__rule {
    position: absolute;
    left: 138px;
    top: 222px;
    width: 560px;
    height: 4px;
    border-radius: 2px;
    background: linear-gradient(90deg, var(--headline) 0%, var(--headline) 45%, rgba(255,255,255,0) 100%);
  }
  .quote-button {
    position: absolute;
    left: 859px;
    top: 279px;
    width: 323px;
    height: 60px;
    box-sizing: border-box;
    border-radius: 11px;
    border: 1px solid var(--button-edge);
    background: linear-gradient(180deg, var(--button-top) 0%, #e4983f 50%, var(--button-bottom) 100%);
    box-shadow: 0 3px 8px rgba(30, 14, 4, 0.5), inset 0 1px 0 rgba(255,255,255,0.45);
    display: flex;
    align-items: center;
    padding-left: 16px;
    gap: 12px;
    text-decoration: none;
  }
  .quote-button__label {
    font-size: 40px;
    font-weight: 700;
    letter-spacing: -0.5px;
    color: #ffffff;
    text-shadow: 0 2px 3px rgba(60, 28, 4, 0.8);
  }
  .quote-button__arrows {
    display: block;
  }
</style>
</head>
<body>
  <main class="banner">
    <div class="banner__decking" role="img" aria-label="Diagonal ipe hardwood deck boards in warm brown tones"></div>
    <h1 class="banner__headline">IPE Wood Decking</h1>
    <div class="banner__rule"></div>
    <a class="quote-button" href="#quote">
      <span class="quote-button__label">Get a Quote!</span>
      <svg class="quote-button__arrows" width="78" height="26" viewBox="0 0 78 26" aria-hidden="true">
        <polygon points="0,1 22,13 0,25" fill="var(--arrow)" opacity="0.75"/>
        <polygon points="27,1 49,13 27,25" fill="var(--arrow)" opacity="0.85"/>
        <polygon points="54,1 76,13 54,25" fill="var(--arrow)"/>
      </svg>
    </a>
  </main>
</body>
</html>
```